Billboard Design for Brightway Home Dentistry

Pinecrest Kinfolk Dental Care
Phone number: 318-572-0934
Address: 482 Coldbrook Blvd
Hours: 7am-5pm ; Monday-Friday

Dental Implant Surgery
Same Day Emergency Visits
Cosmetic Treatments
GLINT! Whitening

NAMES: Dr. Calvin Brastedder
Dr. Peter Haskell

MOST INSURANCES ACCEPTED

Eye catching slogan/colors/design for billboard

Our website is www.pinecrestkinfolkdentalcare.example to see current branding.

Target Market(s)

Target market is anyone in Alexandria. Focus on Families and High End Cosmetic Dentistry.

Industry/Entity Type

Dental Clinic

Requirements
Must have
• Pinecrest Kinfolk Dental Care
• Phone number: 318-572-0934
• Address: 482 Coldbrook Blvd
• Hours: 7am-5pm ; Monday-Friday
• Dental Implant Surgery
• Same Day Emergency Visits
• Cosmetic Treatments
• GLINT! Whitening
• NAMES: Dr. Calvin Brastedder
• Dr. Peter Haskell
• and logo
Nice to have
• digital billboard-try to catch attention with color or phrase
Should not have
• Can not make claims or compare to other area dentist's according to laws.

```html
<!DOCTYPE html>
<html lang="en">
<head>
<meta charset="utf-8">
<title>Brightway Home Dentistry — Billboard</title>
<link rel="stylesheet" href="https://fonts.googleapis.com/css2?family=Montserrat:wght@600&family=Quicksand:wght@300;500&family=Raleway:wght@300&display=swap">
<style>
  :root {
    --paper: #ffffff;
    --brand-cyan: #3cb6d6;
    --brand-slate: #5b6b80;
    --brand-grey: #9aa3ab;
    --body-grey: #6f7478;
    --board-teal: #45b7c5;
    --board-frame: #a9adb1;
    --board-text: #6a8796;
    --board-names: #4d5e72;
    --white: #ffffff;
  }
  * { box-sizing: border-box; margin: 0; padding: 0; }
  html, body { width: 848px; height: 1200px; overflow: hidden; background: var(--paper); }
  .canvas { position: relative; width: 848px; height: 1200px; background: var(--paper); }

  /* Brand lockup */
  .brand-mark {
    position: absolute; left: 0; width: 848px;
    display: flex; align-items: center; justify-content: center; gap: 14px;
    font-family: "Quicksand", sans-serif; font-weight: 500;
  }
  .brand-mark .dot { border-radius: 50%; background: var(--brand-cyan); flex: none; }
  .brand-mark--print { top: 78px; font-size: 34px; color: var(--brand-grey); }
  .brand-mark--print .dot { width: 26px; height: 26px; }
  .brand-mark--board {
    top: 708px; gap: 10px;
    font-size: 22px; line-height: 25px; color: var(--white);
  }
  .brand-mark--board .name { max-width: 180px; text-align: left; }
  .brand-mark--board .dot { width: 18px; height: 18px; background: var(--board-names); }

  .clinic-title {
    position: absolute; left: 0; width: 848px; text-align: center;
    font-family: "Quicksand", sans-serif; font-weight: 300; line-height: 1;
  }
  .clinic-title--print { top: 182px; font-size: 58px; color: var(--brand-cyan); }
  .clinic-title--board { top: 800px; font-size: 40px; color: var(--white); }

  /* Details lists */
  .detail-list {
    position: absolute; list-style: none;
    font-family: "Raleway", sans-serif; font-weight: 300;
  }
  .detail-list li::before { content: "- "; }
  .detail-list--contact-print { left: 161px; top: 274px; font-size: 15.5px; line-height: 22px; color: var(--body-grey); }
  .detail-list--services-print { left: 450px; top: 268px; font-size: 15.5px; line-height: 22px; color: var(--body-grey); }
  .detail-list--contact-board { left: 58px; top: 690px; font-size: 14px; line-height: 18.5px; color: var(--board-text); }
  .detail-list--services-board { left: 590px; top: 690px; font-size: 14px; line-height: 18.5px; color: var(--board-text); }

  .doctor-names {
    position: absolute; left: 0; width: 848px; text-align: center;
    font-family: "Montserrat", sans-serif; font-weight: 600;
  }
  .doctor-names--print { top: 374px; font-size: 35px; line-height: 46px; color: var(--brand-slate); }
  .doctor-names--board { top: 850px; font-size: 23px; line-height: 32px; color: var(--board-names); }

  /* Billboard face */
  .billboard {
    position: absolute; left: 43px; top: 668px; width: 770px; height: 266px;
    background: var(--board-teal);
    border: 8px solid var(--board-frame);
  }
</style>
</head>
<body>
<main class="canvas">

  <section class="print-layout">
    <div class="brand-mark brand-mark--print"><span class="dot"></span><span class="name">Brightway Home Dentistry</span></div>
    <h1 class="clinic-title clinic-title--print">Dental Clinic</h1>

    <ul class="detail-list detail-list--contact-print">
      <li>Pinecrest Kinfolk Dental Care</li>
      <li>Phone number: 318-572-0934</li>
      <li>Address: 482 Coldbrook Blvd</li>
      <li>Hours: 7am-5pm ; Monday-Friday</li>
    </ul>
    <ul class="detail-list detail-list--services-print">
      <li>Dental Implant Surgery</li>
      <li>Same Day Emergency Visits</li>
      <li>Cosmetic Treatments</li>
      <li>GLINT! Whitening</li>
    </ul>

    <p class="doctor-names doctor-names--print">Dr. Calvin Brastedder<br>Dr. Peter Haskell</p>
  </section>

  <section class="billboard-layout">
    <div class="billboard"></div>

    <ul class="detail-list detail-list--contact-board">
      <li>Pinecrest Kinfolk Dental Care</li>
      <li>Phone number: 318-572-0934</li>
      <li>Address: 482 Coldbrook Blvd</li>
      <li>Hours: 7am-5pm ; Monday-Friday</li>
    </ul>
    <ul class="detail-list detail-list--services-board">
      <li>Dental Implant Surgery</li>
      <li>Same Day Emergency Visits</li>
      <li>Cosmetic Treatments</li>
      <li>GLINT! Whitening</li>
    </ul>

    <div class="brand-mark brand-mark--board"><span class="dot"></span><span class="name">Brightway Home Dentistry</span></div>
    <h2 class="clinic-title clinic-title--board">Dental Clinic</h2>
    <p class="doctor-names doctor-names--board">Dr. Calvin Brastedder<br>Dr. Peter Haskell</p>
  </section>

</main>
</body>
</html>
```